KORVEL Consulting Trucking Business Card

Our company name is KORVEL Consulting.

We need a business card design for our trucking company. The design should communicate reliability, stability and resourcefulness. The design should be clean, modern and industrial.

Audience will be US clients/prospects that require trucking to ship their products.

Target Market(s)

US businesses that needs trucks to ship products

Industry/Entity Type

Business

Font styles to use
Sans Serif

Colors
85cae6
3176b5
b7a5cd
85acd3
33a6d7

```html
<!DOCTYPE html>
<html lang="en">
<head>
<meta charset="utf-8">
<title>KORVEL Consulting – Business Card</title>
<link href="https://fonts.googleapis.com/css2?family=Roboto:wght@100;300;400;700&display=swap" rel="stylesheet">
<style>
  :root {
    --brand-blue: #3176b5;
    --brand-lilac: #b7a5cd;
    --paper: #ffffff;
    --ink: #3a3a3a;
    --rule: #8a8a8a;
  }
  html, body {
    margin: 0;
    padding: 0;
    overflow: hidden;
    background: var(--paper);
  }
  .card {
    position: relative;
    width: 681px;
    height: 1200px;
    background: var(--paper);
    overflow: hidden;
    font-family: "Roboto", "Helvetica Neue", Arial, sans-serif;
  }
  .truck-art {
    position: absolute;
    left: 0;
    top: 124px;
    width: 622px;
    height: 440px;
    background: var(--brand-blue);
    border-radius: 0 40px 60px 0;
  }
  .wordmark {
    position: absolute;
    left: 41px;
    top: 252px;
    margin: 0;
    font-weight: 400;
    line-height: 1;
  }
  .wordmark-name {
    display: block;
    font-weight: 700;
    font-size: 70px;
    color: var(--paper);
    letter-spacing: 1px;
  }
  .wordmark-tagline {
    display: block;
    margin-top: 28px;
    font-weight: 100;
    font-size: 77px;
    color: var(--brand-lilac);
    letter-spacing: 0;
  }
  .divider {
    position: absolute;
    left: 41px;
    right: 0;
    top: 568px;
    height: 0;
    border-top: 2px solid var(--rule);
  }
  .contact {
    position: absolute;
    left: 41px;
    top: 602px;
    margin: 0;
    padding: 0;
    list-style: none;
    font-weight: 300;
    font-size: 31px;
    line-height: 37px;
    color: var(--ink);
  }
</style>
</head>
<body>
  <main class="card">
    <div class="truck-art" role="img" aria-label="Blue delivery truck silhouette illustration"></div>
    <h1 class="wordmark">
      <span class="wordmark-name">KORVEL</span>
      <span class="wordmark-tagline">CONSULTING</span>
    </h1>
    <div class="divider"></div>
    <ul class="contact">
      <li>Adress 1</li>
      <li>Phone Number</li>
      <li>website, etc</li>
      <li>Anything else you might</li>
      <li>want to add</li>
    </ul>
  </main>
</body>
</html>
```